Pomar Veloz - Working hours register App needs interface design

Pomar Veloz, a 1 million users Brazilian website focused on general calculations needs an interface to an App for registering the working hours of a housemaid, a nanny, a housekeeper or other domestic workers.
The final users should be mainly housewifes.
The wireframe of the pages is in the Tirvel_layout.xls file attached.
Logo is also available in the wireframe.
The interface should be optimized for Android on Nimbus QX with a 5'' screen.
Target Market(s)
Females, educated, from 30 to 50 y.o.
Industry/Entity Type
Android

```html
<!DOCTYPE html>
<html lang="en">
<head>
<meta charset="utf-8">
<title>Pomar Veloz - Tirvel · Punch In</title>
<link rel="stylesheet" href="https://fonts.googleapis.com/css2?family=Roboto+Condensed:wght@300;400;700&display=swap">
<style>
  :root{
    --page:#e6e6e6;
    --status:#0d0d0d;
    --header-top:#3a3d42;
    --header-bottom:#24262a;
    --accent:#c8102e;
    --band-top:#575a5f;
    --band-bottom:#45484d;
    --sheet:#f1f1f1;
    --card:#e9e9e9;
    --row-line:#cfcfcf;
    --text:#4a4a4a;
    --muted:#8a8a8a;
    --button:#55585d;
    --white:#ffffff;
  }
  *{box-sizing:border-box;margin:0;padding:0}
  html,body{width:1200px;height:849px;overflow:hidden;background:var(--page)}
  body{font-family:"Roboto Condensed",Arial,sans-serif;color:var(--text);position:relative}
  .screen{position:absolute;left:380px;top:18px;width:440px;height:813px;background:var(--sheet);overflow:hidden;box-shadow:0 2px 10px rgba(0,0,0,.15)}
  .status-bar{height:28px;background:var(--status);color:var(--white);display:flex;align-items:center;padding:0 10px;font-size:15px;font-weight:700;position:relative}
  .status-bar .signal{margin-right:6px}
  .status-bar .lock{position:absolute;left:212px;top:6px}
  .status-bar .battery{position:absolute;right:10px;top:8px}
  .app-header{height:76px;background:linear-gradient(var(--header-top),var(--header-bottom));border-bottom:2px solid var(--accent);display:flex;align-items:center;padding:0 10px;gap:10px}
  .brand-square{width:52px;height:52px;background:var(--accent);border-radius:4px;flex:none}
  .app-title{color:var(--white);font-size:24px;font-weight:400;flex:1;white-space:nowrap}
  .return-button{background:linear-gradient(#7a7d82,#4e5156);color:var(--white);border:1px solid #2a2c30;border-radius:5px;font:inherit;font-size:17px;padding:7px 10px}
  .page-band{height:58px;background:linear-gradient(var(--band-top),var(--band-bottom));border-bottom:2px solid var(--accent);color:var(--white);font-size:23px;display:flex;align-items:center;justify-content:center}
  .employee{height:100px;display:flex;align-items:flex-start;padding:6px 12px;gap:22px;border-bottom:1px solid var(--row-line);background:var(--sheet)}
  .employee-photo{width:88px;height:88px;border:1px solid #bbb;background:linear-gradient(#8a6a5a,#5a3e34)}
  .employee-name{font-size:21px;color:var(--text);margin-top:2px}
  .employee-meta{font-size:17px;color:var(--muted);margin-top:4px;line-height:1.55}
  .card{margin:8px 8px 0;background:var(--card);border:1px solid #cdcdcd;border-radius:4px;box-shadow:0 1px 2px rgba(0,0,0,.15)}
  .card-title{height:36px;color:var(--accent);font-size:20px;display:flex;align-items:center;justify-content:center;border-bottom:1px solid var(--row-line)}
  .clock-row{height:54px;display:flex;align-items:center;justify-content:center;position:relative;border-bottom:1px solid var(--row-line);font-size:34px;font-weight:300;color:#555}
  .clock-row .icon-button{position:absolute;right:8px;top:9px}
  .row{height:49px;display:flex;align-items:center;padding:0 10px;border-bottom:1px solid var(--row-line)}
  .row:last-child{border-bottom:none}
  .row-label{flex:1;font-size:18px;color:var(--text)}
  .row-value{font-size:23px;color:#555}
  .row .icon-button{margin-left:12px}
  .icon-button{display:block}
</style>
</head>
<body>
  <main class="screen">
    <div class="status-bar">
      <svg class="signal" width="22" height="12" viewBox="0 0 22 12"><g fill="#fff"><rect x="0" y="9" width="3" height="3"/><rect x="4" y="7" width="3" height="5"/><rect x="8" y="5" width="3" height="7"/><rect x="12" y="3" width="3" height="9"/><rect x="16" y="0" width="3" height="12"/></g></svg>
      <span>ORBITA&nbsp; 3G</span>
      <svg class="lock" width="12" height="15" viewBox="0 0 12 15"><path d="M3 7V4.5a3 3 0 0 1 6 0V7" fill="none" stroke="#fff" stroke-width="2"/><rect x="0.5" y="7" width="11" height="8" rx="1" fill="#fff"/></svg>
      <svg class="battery" width="28" height="12" viewBox="0 0 28 12"><rect x="0.5" y="0.5" width="24" height="11" rx="2" fill="none" stroke="#fff"/><rect x="2.5" y="2.5" width="20" height="7" fill="#fff"/><rect x="25" y="4" width="2.5" height="4" fill="#fff"/></svg>
    </div>

    <header class="app-header">
      <span class="brand-square"></span>
      <h1 class="app-title">Pomar Veloz - Tirvel</h1>
      <button class="return-button">Return</button>
    </header>

    <div class="page-band">Punch In</div>

    <section class="employee">
      <div class="employee-photo" role="img" aria-label="Employee portrait photo"></div>
      <div>
        <div class="employee-name">Employee 1</div>
        <div class="employee-meta">Date : 25-Jan<br>Week Day</div>
      </div>
    </section>

    <section class="card punch-card">
      <div class="card-title">Hour</div>
      <div class="clock-row">9:31:31
        <svg class="icon-button" width="36" height="36" viewBox="0 0 36 36"><circle cx="18" cy="18" r="17" fill="var(--button)"/><circle cx="17" cy="18" r="9" fill="none" stroke="#fff" stroke-width="2"/><path d="M17 13v5h4" fill="none" stroke="#fff" stroke-width="2"/><circle cx="25" cy="25" r="5" fill="#fff"/><path d="M25 22v6M22 25h6" stroke="var(--button)" stroke-width="1.6"/></svg>
      </div>
      <div class="row"><span class="row-label">Arrival</span><span class="row-value">9:00</span><svg class="icon-button" width="44" height="28" viewBox="0 0 44 28"><rect width="44" height="28" rx="14" fill="var(--button)"/><circle cx="22" cy="14" r="8" fill="none" stroke="#fff" stroke-width="1.8"/><path d="M22 9v5h4" fill="none" stroke="#fff" stroke-width="1.8"/></svg></div>
      <div class="row"><span class="row-label">Lunch Break Start</span><span class="row-value">12:00</span><svg class="icon-button" width="44" height="28" viewBox="0 0 44 28"><rect width="44" height="28" rx="14" fill="var(--button)"/><circle cx="22" cy="14" r="8" fill="none" stroke="#fff" stroke-width="1.8"/><path d="M22 9v5h4" fill="none" stroke="#fff" stroke-width="1.8"/></svg></div>
      <div class="row"><span class="row-label">Lunch Break End</span><span class="row-value">12:30</span><svg class="icon-button" width="44" height="28" viewBox="0 0 44 28"><rect width="44" height="28" rx="14" fill="var(--button)"/><circle cx="22" cy="14" r="8" fill="none" stroke="#fff" stroke-width="1.8"/><path d="M22 9v5h4" fill="none" stroke="#fff" stroke-width="1.8"/></svg></div>
      <div class="row"><span class="row-label">Out</span><span class="row-value">17:30</span><svg class="icon-button" width="44" height="28" viewBox="0 0 44 28"><rect width="44" height="28" rx="14" fill="var(--button)"/><circle cx="22" cy="14" r="8" fill="none" stroke="#fff" stroke-width="1.8"/><path d="M22 9v5h4" fill="none" stroke="#fff" stroke-width="1.8"/></svg></div>
    </section>

    <section class="card report-card">
      <div class="card-title">Employee Monthly Report</div>
      <div class="row"><span class="row-label">Working Hours</span><span class="row-value">8:00</span></div>
      <div class="row"><span class="row-label">Compensated Hour</span><span class="row-value">0:30</span></div>
      <div class="row"><span class="row-label">Extra Hours</span><span class="row-value">0:00</span></div>
      <div class="row"><span class="row-label">Night Extra Hours</span><span class="row-value">0:00</span></div>
    </section>
  </main>
</body>
</html>
```